Professional violinist needs business cards

I am trying to attract the following jobs:
-private violin lessons (primarily classical)
-performance gigs (weddings, birthday parties, funerals, etc.)
-collaborations with other artists (studio recordings, performances)

I want to communicate that I have a very high standard of excellence for my work, but I also love people and celebrations.
Values/style words I like are:
love, joy, peace, fun, beauty, authenticity, excellence, warmth, refined/sleek, free spirited. If that's too confusing, just ignore :)

I will attach my favorite business card template that I could find on Canva. The lines are supposed to be like a music staff, which I think is really cool, but I also don't want it to look too busy. I like the simple black and white--I think it looks sharp--but I also am open to other ideas. I also have seen business cards with pictures included that looked great, so I attached an image that could be used as well.

I am also attaching a file that I made of my initials that could be used as a logo, but I'm not sure if it should be included.

Information on the card:
-My name (18 letters total)
-"violinist"
-phone number, email, website

Thank you!

```html
<!DOCTYPE html>
<html lang="en">
<head>
<meta charset="UTF-8">
<title>Josephine Whitaker — Violinist Business Card</title>
<link href="https://fonts.googleapis.com/css2?family=Barlow+Semi+Condensed:wght@400;500;600&family=Barlow:wght@400;500&display=swap" rel="stylesheet">
<style>
  :root {
    --canvas: #e6e2dc;
    --card-white: #f6f6f6;
    --card-black: #030303;
    --ink: #141414;
    --ink-soft: #3a3a3a;
    --silver-light: #d9d9d9;
    --silver-dark: #7b7b7b;
    --photo-light: #cfcfcf;
    --photo-mid: #7a7a7a;
    --photo-dark: #262626;
  }
  * { margin: 0; padding: 0; box-sizing: border-box; }
  html, body { width: 1200px; height: 1200px; overflow: hidden; }
  body {
    background: var(--canvas);
    display: flex;
    flex-direction: column;
    align-items: center;
    justify-content: center;
    gap: 56px;
  }
  .card {
    width: 900px;
    height: 514px;
    position: relative;
    overflow: hidden;
    box-shadow: 0 3px 10px rgba(0,0,0,0.18);
  }

  /* Front */
  .card-front { background: var(--card-white); }
  .portrait {
    position: absolute;
    top: 0; right: 0;
    width: 520px; height: 100%;
    background:
      radial-gradient(ellipse 40% 55% at 62% 45%, var(--photo-dark) 0%, rgba(38,38,38,0) 70%),
      linear-gradient(100deg, var(--photo-light) 0%, var(--photo-mid) 45%, var(--photo-dark) 100%);
    -webkit-mask-image: linear-gradient(90deg, transparent 0%, #000 28%);
            mask-image: linear-gradient(90deg, transparent 0%, #000 28%);
  }
  .identity {
    position: absolute;
    left: 66px; top: 118px;
    font-family: "Barlow Semi Condensed", sans-serif;
    color: var(--ink);
  }
  .identity-name {
    font-size: 38px;
    line-height: 1;
    letter-spacing: 0.5px;
    text-transform: uppercase;
  }
  .identity-name .first { font-weight: 600; }
  .identity-name .last { font-weight: 400; }
  .identity-role {
    margin-top: 12px;
    font-size: 18px;
    font-weight: 400;
    letter-spacing: 6px;
    text-transform: uppercase;
    color: var(--ink-soft);
  }
  .contacts {
    position: absolute;
    left: 66px; top: 272px;
    list-style: none;
    font-family: "Barlow", sans-serif;
    font-size: 23px;
    font-weight: 500;
    color: var(--ink);
  }
  .contacts li {
    display: flex;
    align-items: center;
    gap: 22px;
    height: 50px;
  }
  .contact-icon { width: 24px; height: 24px; flex: none; }

  /* Back */
  .card-back {
    background: var(--card-black);
    display: flex;
    align-items: center;
    justify-content: center;
    gap: 22px;
  }
  .wordmark-dot {
    width: 16px; height: 16px;
    border-radius: 50%;
    background: var(--silver-light);
  }
  .wordmark {
    font-family: "Barlow Semi Condensed", sans-serif;
    font-weight: 500;
    font-size: 52px;
    letter-spacing: 4px;
    text-transform: uppercase;
    color: var(--silver-light);
  }
</style>
</head>
<body>

  <section class="card card-front">
    <div class="portrait" role="img" aria-label="Black and white portrait of the violinist holding her violin and bow in front of a brick wall, with a brushed, splattered left edge"></div>

    <div class="identity">
      <h1 class="identity-name"><span class="first">Josephine</span> <span class="last">Whitaker</span></h1>
      <p class="identity-role">Violinist</p>
    </div>

    <ul class="contacts">
      <li>
        <svg class="contact-icon" viewBox="0 0 24 24" aria-hidden="true">
          <path fill="#141414" d="M6.6 2.5c.6-.4 1.4-.2 1.8.4l2 3.2c.3.6.2 1.3-.3 1.7l-1.5 1.2c.9 2.2 2.5 4.1 4.5 5.4l1.3-1.4c.4-.5 1.1-.6 1.7-.2l3.1 2.1c.6.4.8 1.2.4 1.8l-1.2 2c-.6.9-1.7 1.4-2.8 1.1C9.7 18.2 5.3 13.2 4.1 7.2c-.2-1.1.3-2.1 1.2-2.7z"/>
        </svg>
        <span>(555) 218 - 0437</span>
      </li>
      <li>
        <svg class="contact-icon" viewBox="0 0 24 24" aria-hidden="true">
          <rect x="1.5" y="5" width="21" height="14" fill="#141414"/>
          <path d="M2.5 6l9.5 7.5L21.5 6" fill="none" stroke="#f6f6f6" stroke-width="1.4"/>
        </svg>
        <span>josephinewhitakerviolin@mail.com</span>
      </li>
      <li>
        <svg class="contact-icon" viewBox="0 0 24 24" aria-hidden="true">
          <circle cx="12" cy="12" r="10" fill="#141414"/>
          <g fill="none" stroke="#f6f6f6" stroke-width="1">
            <ellipse cx="12" cy="12" rx="4.5" ry="10"/>
            <line x1="2" y1="12" x2="22" y2="12"/>
            <line x1="12" y1="2" x2="12" y2="22"/>
            <path d="M4 7h16M4 17h16"/>
          </g>
        </svg>
        <span>www.josephinewhitaker.com</span>
      </li>
    </ul>
  </section>

  <section class="card card-back">
    <span class="wordmark-dot"></span>
    <span class="wordmark">Josephine Whitaker</span>
  </section>

</body>
</html>
```